Horse related business entrepreneur needs a business card

I need a business card design for my horse related business. The enterprise is Copper Vale LLC and I have 3 businesses (headquartered at 2 locations): 1. property management where we rent horse stalls and apartments at a thoroughbred training center outside Ocala; 2. a medium sized transportation service in central Florida that sells horse bedding and removes used horse bedding from horse farms; and horse racing

```html
<!DOCTYPE html>
<html lang="en">
<head>
<meta charset="utf-8">
<title>Copper Vale LLC – Business Card</title>
<link rel="stylesheet" href="https://fonts.googleapis.com/css2?family=Cinzel:wght@500;600&family=Crimson+Pro:ital,wght@1,400&family=Tinos&family=Roboto:wght@400&display=swap">
<style>
  :root {
    --backdrop: #2b2b2b;
    --card-white: #ffffff;
    --teal: #055672;
    --copper: #e07046;
    --ink-grey: #555555;
    --address-white: #f2f5f7;
    --rule-light: rgba(255, 255, 255, 0.75);
  }
  * { margin: 0; padding: 0; box-sizing: border-box; }
  html, body {
    width: 1125px;
    height: 1200px;
    overflow: hidden;
    background: var(--backdrop);
  }
  .canvas {
    position: relative;
    width: 1125px;
    height: 1200px;
  }
  .card {
    position: absolute;
    left: 150px;
    width: 826px;
    height: 471px;
    overflow: hidden;
  }
  .card--front { top: 98px; background: var(--card-white); }
  .card--back { top: 631px; background: var(--teal); }

  /* Front */
  .running-horse-art {
    position: absolute;
    left: 480px;
    top: 14px;
    width: 346px;
    height: 430px;
    background: linear-gradient(180deg, var(--copper) 0%, var(--copper) 72%, var(--teal) 100%);
  }
  .holder-name {
    position: absolute;
    left: 51px;
    top: 244px;
    font-family: "Cinzel", serif;
    font-weight: 600;
    font-size: 30px;
    line-height: 34px;
    color: var(--teal);
    white-space: nowrap;
  }
  .holder-role {
    position: absolute;
    left: 51px;
    top: 277px;
    font-family: "Cinzel", serif;
    font-weight: 600;
    font-size: 19px;
    line-height: 22px;
    color: var(--copper);
  }
  .company-block, .contact-block {
    position: absolute;
    left: 51px;
    font-family: "Tinos", serif;
    font-size: 18px;
    line-height: 26px;
    color: var(--ink-grey);
    white-space: nowrap;
  }
  .company-block { top: 312px; }
  .contact-block { top: 373px; }

  /* Back */
  .farm-emblem-art {
    position: absolute;
    left: 242px;
    top: 117px;
    width: 258px;
    height: 100px;
    background: var(--card-white);
  }
  .farm-rule {
    position: absolute;
    left: 270px;
    top: 233px;
    width: 284px;
    height: 0;
    border-top: 1.5px solid var(--rule-light);
  }
  .farm-name {
    position: absolute;
    left: 0;
    width: 100%;
    top: 242px;
    text-align: center;
    font-family: "Cinzel", serif;
    font-weight: 600;
    font-size: 37px;
    letter-spacing: 2px;
    line-height: 44px;
    color: var(--card-white);
    white-space: nowrap;
  }
  .farm-location {
    position: absolute;
    left: 0;
    width: 100%;
    top: 290px;
    text-align: center;
    font-family: "Crimson Pro", serif;
    font-style: italic;
    font-size: 29px;
    line-height: 34px;
    color: var(--card-white);
  }
  .farm-addresses {
    position: absolute;
    left: 0;
    width: 100%;
    top: 372px;
    text-align: center;
    font-family: "Roboto", sans-serif;
    font-size: 20px;
    line-height: 27px;
    color: var(--address-white);
    white-space: nowrap;
  }
</style>
</head>
<body>
<main class="canvas">
  <section class="card card--front">
    <div class="running-horse-art" role="img" aria-label="Copper-coloured galloping horse silhouette with a teal shadow beneath"></div>
    <h1 class="holder-name">Dana Whitlock</h1>
    <p class="holder-role">Owner</p>
    <p class="company-block">Copper Vale LLC<br>(an equine conglomerate)</p>
    <p class="contact-block">P. (434) 555-0147 F. (434) 555-0182<br>E. dana@coppervale.com W. www.coppervale.com</p>
  </section>

  <section class="card card--back">
    <div class="farm-emblem-art" role="img" aria-label="White galloping horse silhouette"></div>
    <div class="farm-rule"></div>
    <p class="farm-name">COPPER VALE FARM</p>
    <p class="farm-location">Morriston FL</p>
    <p class="farm-addresses">1725 SE 152nd Lane, Morriston, FL 32668<br>880 Hollow Creek Road, Charlottesville, VA 22903</p>
  </section>
</main>
</body>
</html>
```